Dog Snacks brand needs a new packaging design

Dear Designers,

We are looking for a packaging expert to design our new line of Dog Snacks which contain a relaxing hemp extract (CBD).

Our company is already selling various relaxing cat & dog products , and we would like this new design to reflect the same "style & feeling" as our current products (see attached instructions).

Technical aspects:
- The packaging is a Stand Up Pouch (12x18.5x7cm - see attached instructions).
- Please follow technical guidelines from printer (see attached instructions).
- The packaging will contain 120g of high-quality, semi-moist dog snacks.
- We will be designing 3 differents variations for 3 different flavours: Chicken, Beef & Liver.
- The packaging will be printed with a matt finish.

Design aspects:
- The design should be compatible with our brand identity (i.e. fluffly, pure, relaxing, positive, clean & natural).
- Soft/rounded shapes are preferred.
- Please use our brand's colors (#3BA384, White & Black).
- Please use our company logo (see attached instructions).
- The design also needs to convey a strong sense of professionalism as we are an animal "healthcare" brand.
- If you want to include a dog picture, we would prefer you to use a picture of our official brand ambassador (see attached instructions).
- We have attached a number of packaging examples which we like a lot. (see attached instructions). Please only use those as general inspiration.
- Only original work (no plagiarism will be accepted).

Please don't hesitate to send us a message if you have any questions about the brand, the product or the design requirements.

We look forward to seeing your designs & working on this together !

Thanks & regards,
Marcus

Target Market(s)

Dog owners

Industry/Entity Type

Pet Care

Font styles to use
Sans Serif

Requirements
Must have
• Please see project description.
Nice to have
Should not have

```html
<!DOCTYPE html>
<html lang="en">
<head>
<meta charset="utf-8">
<title>Snoozlets Chicken CBD Treats – Pouch Front</title>
<link href="https://fonts.googleapis.com/css2?family=Open+Sans:wght@300;400;600;700&display=swap" rel="stylesheet">
<style>
  :root {
    --brand-green: #42956a;
    --ink: #111111;
    --grey-text: #6f6f6f;
    --rule: #8a8a8a;
    --paper: #ffffff;
    --dog-light: #e9e7e6;
    --dog-shade: #b9b4b3;
  }
  * { margin: 0; padding: 0; box-sizing: border-box; }
  html, body { width: 1177px; height: 1200px; overflow: hidden; background: var(--paper); }
  body { font-family: "Open Sans", Arial, sans-serif; }
  .pouch-front { position: relative; width: 1177px; height: 1200px; background: var(--paper); }

  .name-ribbon {
    position: absolute; left: 339px; top: 56px; width: 123px; height: 787px;
    background: var(--brand-green);
    border-radius: 0 0 62px 62px;
  }
  .product-line {
    position: absolute; left: 368px; top: 796px;
    transform-origin: 0 0;
    transform: rotate(-90deg);
    white-space: nowrap;
    color: var(--paper);
    font-weight: 300; font-size: 58px; line-height: 64px; letter-spacing: 13px;
  }
  .product-line sup {
    font-size: 18px; letter-spacing: 0; line-height: 0;
    position: relative; top: -30px; vertical-align: baseline;
  }

  .brand-mark {
    position: absolute; left: 576px; top: 345px; width: 204px;
    text-align: center;
  }
  .brand-mark .dot {
    display: block; width: 44px; height: 44px; margin: 0 auto 18px;
    border-radius: 50%; background: var(--brand-green);
  }
  .brand-mark .brand-name {
    font-weight: 600; font-size: 40px; line-height: 1; color: var(--ink); letter-spacing: 1px;
  }

  .flavour-block { position: absolute; left: 581px; top: 548px; width: 193px; text-align: center; }
  .flavour { color: var(--brand-green); font-weight: 700; font-size: 32px; line-height: 40px; }
  .category {
    color: var(--brand-green); font-weight: 700; font-size: 28px; line-height: 36px;
    letter-spacing: 3px; margin-top: 6px; white-space: nowrap;
  }
  .rule { height: 1px; background: var(--rule); }
  .rule.top { margin-top: 9px; }
  .benefits {
    color: var(--grey-text); font-size: 16.5px; line-height: 44px; white-space: nowrap;
  }
  .specs {
    display: flex; justify-content: space-between;
    color: var(--grey-text); font-size: 14px; line-height: 34px;
  }

  .ambassador-photo {
    position: absolute; left: 649px; top: 776px; width: 210px; height: 265px;
    border-radius: 100px 100px 0 0;
    background: radial-gradient(ellipse at 50% 40%, var(--dog-light) 0%, #d4d0cf 60%, var(--dog-shade) 100%);
  }

  .endorsement {
    position: absolute; left: 339px; top: 996px;
    font-size: 16.5px; color: var(--ink); white-space: nowrap;
  }

  .base-band {
    position: absolute; left: 239px; top: 1041px; width: 698px; height: 92px;
    background: var(--brand-green);
  }
</style>
</head>
<body>
  <main class="pouch-front">
    <div class="name-ribbon"></div>
    <div class="product-line">Snoozlets<sup>TM</sup></div>

    <div class="brand-mark">
      <span class="dot"></span>
      <div class="brand-name">VERDALO</div>
    </div>

    <section class="flavour-block">
      <h1 class="flavour">Chicken</h1>
      <h2 class="category">CBD TREATS</h2>
      <div class="rule top"></div>
      <p class="benefits">SUPPORT | CALM | EASE</p>
      <div class="rule"></div>
      <p class="specs"><span>120g</span><span>CBD 250mg</span><span>0% THC</span></p>
    </section>

    <div class="ambassador-photo" role="img" aria-label="Photo of the brand ambassador, a white wrinkled dog with eyes closed"></div>

    <p class="endorsement">Recommended by veterinarians</p>

    <div class="base-band" role="img" aria-label="Green band with a white paw print pattern"></div>
  </main>
</body>
</html>
```